Medical IT Business with New logo needs a fresh stationary design

First time on pixel Harbor; Thought I would give it a go.
This project is for business cards alone but we have loads of design work that needs to take place in the immediate future.

We provide IT services to the Medical Industry and value ourselves as offering a premium product to the market.

I am after a fresh, clean design using full colour 2 sided cards which includes our current colour palettes from our logo.

Card's must include:
- Logo
- Slogan
- Name
- Adress
- Email
- Phone
- Fax
- Mobile

Target Market(s)

Surgeons, High Profile Medical Personnel

Industry/Entity Type

Business

Fonts, CMYK Colours and Logo files attached.

Requirements
Must have
• Card's must include:
• - Logo
• - Slogan
• - Name
• - Adress
• - Email
• - Phone
• - Fax
• - Mobile
Nice to have
• Needs to incorporate our colour palette (attached CMYK colours)
Should not have
• Black backgrounds. Black text ok.

```html
<!DOCTYPE html>
<html lang="en">
<head>
<meta charset="utf-8">
<title>Kardiolink Systems – Business Cards</title>
<link href="https://fonts.googleapis.com/css2?family=Open+Sans:wght@400;600;700;800&display=swap" rel="stylesheet">
<style>
  :root{
    --brand-blue:#0a80b8;
    --brand-navy:#0e3a6e;
    --paper:#ffffff;
    --slogan:#8aa3bd;
    --backdrop:#e9ecef;
  }
  *{box-sizing:border-box;margin:0;padding:0}
  html,body{width:1200px;height:900px;overflow:hidden}
  body{
    background:var(--backdrop);
    font-family:"Open Sans",Arial,sans-serif;
    display:flex;flex-direction:column;align-items:center;justify-content:center;gap:40px;
  }
  .card{
    position:relative;width:700px;height:400px;border-radius:26px;overflow:hidden;
    box-shadow:0 10px 30px rgba(0,0,0,.18);
  }
  /* front */
  .card-front{background:var(--brand-blue);display:flex;align-items:center;justify-content:center;gap:28px}
  .front-dot{width:150px;height:150px;border-radius:50%;background:var(--brand-navy)}
  .front-name{color:var(--paper);font-weight:800;font-size:40px;line-height:1.05;letter-spacing:1px}
  /* back */
  .card-back{background:var(--paper)}
  .back-shapes{position:absolute;inset:0;width:100%;height:100%}
  .edge-dot{position:absolute;left:-14px;top:126px;width:28px;height:28px;border-radius:50%;background:var(--brand-blue)}
  .holder-name{position:absolute;left:40px;top:122px;color:var(--brand-navy);font-weight:800;font-size:26px;letter-spacing:.5px}
  .brand{position:absolute;right:40px;top:28px;display:flex;align-items:center;gap:14px}
  .brand-dot{width:66px;height:66px;border-radius:50%;background:var(--brand-blue)}
  .brand-text{color:var(--brand-navy);font-weight:800;font-size:24px;line-height:1.05;letter-spacing:.5px}
  .slogan{display:block;color:var(--slogan);font-weight:400;font-size:12px;letter-spacing:.3px;margin-top:4px}
  .address{position:absolute;right:40px;top:118px;text-align:right;color:var(--brand-blue);font-size:16px;line-height:1.35;font-weight:600}
  .contacts{position:absolute;right:40px;top:236px;list-style:none;text-align:right;color:var(--paper);font-size:16px;line-height:1.5;font-weight:600}
  .contacts li{display:flex;justify-content:flex-end;align-items:center;gap:10px}
  .contacts svg{width:14px;height:14px;flex:none}
  .contacts .email{margin-top:8px}
</style>
</head>
<body>
  <section class="card card-front" aria-label="Card front">
    <div class="front-dot"></div>
    <div class="front-name">KARDIOLINK<br>SYSTEMS</div>
  </section>

  <section class="card card-back" aria-label="Card back">
    <svg class="back-shapes" viewBox="0 0 700 400" preserveAspectRatio="none" aria-hidden="true">
      <polygon points="0,320 240,320 700,170 700,400 0,400" fill="var(--brand-blue)"/>
      <polyline points="0,320 240,320 700,170" fill="none" stroke="var(--brand-navy)" stroke-width="6"/>
    </svg>
    <div class="edge-dot"></div>
    <h1 class="holder-name">MARTEN LOYE</h1>

    <div class="brand">
      <div class="brand-dot"></div>
      <div class="brand-text">KARDIOLINK SYSTEMS<span class="slogan">care-ready IT for clinics</span></div>
    </div>

    <p class="address">48 Harbor Lane<br>Millbrook, NY 12545</p>

    <ul class="contacts">
      <li>+1 845 555 0142
        <svg viewBox="0 0 16 16"><path d="M4 1l3 3-2 2c1 2 3 4 5 5l2-2 3 3-2 3C7 15 1 9 1 3z" fill="none" stroke="currentColor" stroke-width="1.4"/></svg></li>
      <li>+1 845 555 0178
        <svg viewBox="0 0 16 16"><rect x="4" y="1" width="8" height="5" fill="none" stroke="currentColor" stroke-width="1.4"/><rect x="1" y="6" width="14" height="7" rx="1" fill="currentColor"/></svg></li>
      <li>+1 845 555 0193
        <svg viewBox="0 0 16 16"><rect x="4" y="1" width="8" height="14" rx="1.5" fill="none" stroke="currentColor" stroke-width="1.4"/><circle cx="8" cy="12.5" r="1" fill="currentColor"/></svg></li>
      <li class="email">info@kardiolinksystems.com
        <svg viewBox="0 0 16 16"><rect x="1" y="3" width="14" height="10" fill="none" stroke="currentColor" stroke-width="1.4"/><polyline points="1,3 8,9 15,3" fill="none" stroke="currentColor" stroke-width="1.4"/></svg></li>
    </ul>
  </section>
</body>
</html>
```